Big Room Track needs a CD cover!

I need a CD cover for a Big Room track which will be released soon. Please orientate at the cover of any existing track. It would be good to find a design which fits this. Its planned to generate a child of corporate design for upcoming releases. Please find a demo of the track and my logo to use in the cover. The name of the track is not found yet. Please use a short demo text to show where the title could be so I can add it afterwards.

Target Market(s)

Music streaming services. EDM Scene. Festival. Promotion.

Colors

Designer to choose colors to be used in the design.

Requirements
Must have
• Needs to be kind of a corporate design with the existing cover of another released track of mine. (Not the exact picture but use of logo and track title in this font). Needs to match the feel of the track (demo provided).
Nice to have
• Should reflect the energy of the track. Light colors are appreciated.
Should not have
• No kiddy pictures (like comic or something).

```html
<!DOCTYPE html>
<html lang="en">
<head>
<meta charset="utf-8">
<title>Big Room – Release Cover</title>
<link rel="stylesheet" href="https://fonts.googleapis.com/css2?family=Alfa+Slab+One&display=swap">
<style>
  :root {
    --bg: #040404;
    --accent: #c23a7a;
    --ring-light: #e6e2e4;
    --ring-pink: #c98aa8;
    --bloom-core: #3a0620;
    --bloom-mid: #e0208a;
    --bloom-edge: #f55fb0;
    --type: #ffffff;
  }
  html, body {
    margin: 0;
    padding: 0;
    width: 1200px;
    height: 1200px;
    overflow: hidden;
    background: var(--bg);
  }
  .cover {
    position: relative;
    width: 1200px;
    height: 1200px;
    background: var(--bg);
  }
  .cover__art {
    position: absolute;
    inset: 0;
  }
  .cover__title {
    position: absolute;
    left: 0;
    right: 0;
    top: 540px;
    margin: 0;
    text-align: center;
    font-family: "Alfa Slab One", serif;
    font-weight: 400;
    font-size: 112px;
    line-height: 1;
    letter-spacing: 1px;
    color: var(--type);
  }
  .cover__label {
    position: absolute;
    left: 0;
    right: 0;
    top: 1080px;
    margin: 0;
    text-align: center;
    font-family: "Alfa Slab One", serif;
    font-weight: 400;
    font-size: 66px;
    line-height: 1;
    letter-spacing: 4px;
    color: var(--type);
  }
</style>
</head>
<body>
<main class="cover">
  <svg class="cover__art" width="1200" height="1200" viewBox="0 0 1200 1200">
    <defs>
      <radialGradient id="bloom-fill" cx="50%" cy="50%" r="50%">
        <stop offset="0%" stop-color="var(--bloom-core)"/>
        <stop offset="35%" stop-color="var(--bloom-mid)"/>
        <stop offset="80%" stop-color="var(--bloom-edge)"/>
        <stop offset="100%" stop-color="var(--bloom-edge)" stop-opacity="0"/>
      </radialGradient>
      <linearGradient id="ring-fill" x1="0" y1="0" x2="1" y2="1">
        <stop offset="0%" stop-color="var(--ring-light)"/>
        <stop offset="55%" stop-color="var(--ring-light)"/>
        <stop offset="100%" stop-color="var(--ring-pink)"/>
      </linearGradient>
    </defs>

    <g class="corner-lines" stroke="var(--accent)" stroke-width="4" stroke-linecap="butt">
      <line x1="72" y1="70" x2="260" y2="250"/>
      <line x1="86" y1="114" x2="242" y2="262"/>
      <line x1="162" y1="126" x2="273" y2="232"/>

      <line x1="1128" y1="70" x2="940" y2="250"/>
      <line x1="1114" y1="114" x2="958" y2="262"/>
      <line x1="1038" y1="126" x2="927" y2="232"/>

      <line x1="72" y1="1130" x2="260" y2="950"/>
      <line x1="86" y1="1086" x2="242" y2="938"/>
      <line x1="162" y1="1074" x2="273" y2="968"/>

      <line x1="1128" y1="1130" x2="940" y2="950"/>
      <line x1="1114" y1="1086" x2="958" y2="938"/>
      <line x1="1038" y1="1074" x2="927" y2="968"/>
    </g>

    <circle class="bloom" role="img" aria-label="Macro photo of a glowing pink dandelion seed head"
            cx="600" cy="592" r="390" fill="url(#bloom-fill)"/>

    <g class="frame-ring" fill="none" stroke="url(#ring-fill)" stroke-width="5">
      <path d="M667 153 A452 452 0 0 1 995.5 819"/>
      <path d="M946 891 A452 452 0 0 1 275 914"/>
      <path d="M222.6 849 A452 452 0 0 1 514 156"/>
    </g>
  </svg>

  <h1 class="cover__title">BIG ROOM</h1>
  <p class="cover__label">PARALLAX</p>
</main>
</body>
</html>
```